Business Card for new Overseas Property Buying Business

Hi

We need a new business card for our new business.

We are Faraway Nest Seekers. So we search locations on behalf of our clients to find them the ideal home.

These are mainly holiday homes in nice locations - but sometimes people are looking to relocate.

I am looking for a nice simple design - that has some class and professionalism about it. Taking inspiration from our logo.

Text wise I was thinking of maybe having something like. (THE FONT FOR THIS SHOULD BE LIKE THE WRITING IN THE ATTACHMENT WITH THE MAP ON IT)

1)
What does your dream house have (tick all that apply):
swimming pool x
private vineyard x
herb garden x
full sized football pitch x

2)
How to buy a home abroad:

Method 1:
1) Scour internet for suitable estate agents
2) Arrange hectic holiday timetable with multiple agents in multiple languages
3) Fly to destination to find property was not as it seemed
4) Feel frustrated and helpless
OR
Method 2:
Contact your expert home hunter (details overleaf) - and leave the hard work to them

The end result should give people confidence that they are dealing with a professional organisation - and feel like they can place their trust in them. I would want it to drive them to either contact us directly or visit the website.

Please include name (Gordon Marsh), position (founder), contact numbers x 2, email address, website (www.quillan-tarvo.com)

I look forward to seeing your entries.

```html
<!DOCTYPE html>
<html lang="en">
<head>
<meta charset="utf-8">
<title>Faraway Nest Seekers – Business Card</title>
<link rel="stylesheet" href="https://fonts.googleapis.com/css2?family=Gochi+Hand&family=Questrial&display=swap">
<style>
  :root {
    --backdrop: #e8e5e1;
    --card-dark: #4a4440;
    --card-white: #ffffff;
    --orange: #e2582e;
    --orange-soft: #f2a46e;
    --cream: #eadbc6;
    --ink: #4a4440;
    --hand-red: #e8603a;
    --hand-peach: #eea073;
  }
  * { box-sizing: border-box; margin: 0; padding: 0; }
  html, body {
    width: 1200px; height: 784px; overflow: hidden;
    background: var(--backdrop);
  }
  .sheet {
    position: relative; width: 1200px; height: 784px;
    display: flex; align-items: center; justify-content: center; gap: 34px;
  }
  .card {
    position: relative; width: 555px; height: 317px; overflow: hidden;
    box-shadow: 0 6px 18px rgba(0,0,0,.18);
  }

  /* ---------- back of card ---------- */
  .card-back {
    background: var(--card-dark);
    font-family: "Gochi Hand", cursive;
    color: var(--hand-peach);
    padding: 22px 24px;
  }
  .back-mark {
    position: absolute; left: 205px; top: 40px;
    width: 190px; height: 190px; border-radius: 50%;
    background: rgba(226, 88, 46, .12);
    display: flex; align-items: center; justify-content: center;
    font-family: "Questrial", sans-serif; font-size: 17px;
    color: rgba(234, 219, 198, .16); text-align: center;
  }
  .back-text { position: relative; font-size: 14.5px; line-height: 17.5px; }
  .back-text .heading { color: var(--hand-red); font-size: 15.5px; }
  .back-text .underlined { text-decoration: underline; text-underline-offset: 2px; }
  .wishlist { list-style: none; margin-bottom: 10px; }
  .wishlist li { display: flex; align-items: center; gap: 4px; }
  .tick { width: 13px; height: 11px; }
  .method { color: var(--hand-red); }
  .steps { list-style: none; }
  .or { color: var(--hand-red); }

  /* ---------- front of card ---------- */
  .card-front { background: var(--card-white); }
  .front-top {
    position: absolute; left: 0; top: 0; width: 100%; height: 190px;
    display: flex; flex-direction: column; align-items: center; justify-content: center; gap: 12px;
  }
  .brand-dot { width: 58px; height: 58px; border-radius: 50%; background: var(--orange); }
  .brand-name {
    font-family: "Questrial", sans-serif; font-size: 25px; color: var(--ink);
    letter-spacing: .5px;
  }
  .front-stripe {
    position: absolute; left: 0; top: 190px; width: 100%; height: 6px;
    background: var(--orange);
  }
  .front-band {
    position: absolute; left: 0; top: 196px; width: 100%; height: 121px;
    background: var(--card-dark);
    font-family: "Questrial", sans-serif;
  }
  .person {
    position: absolute; left: 128px; top: 38px; text-align: right; width: 130px;
  }
  .person-name { color: var(--orange); font-size: 18px; }
  .person-role { color: var(--cream); font-size: 15px; margin-top: 3px; }
  .divider {
    position: absolute; left: 282px; top: 18px; width: 1px; height: 86px;
    background: var(--orange-soft); opacity: .7;
  }
  .contacts {
    position: absolute; left: 300px; top: 20px; list-style: none;
    color: var(--orange-soft); font-size: 14px; line-height: 20.5px;
  }
  .contacts li { display: flex; align-items: center; gap: 8px; }
  .contact-icon { width: 14px; height: 14px; flex: none; }
</style>
</head>
<body>
<main class="sheet">

  <!-- back -->
  <section class="card card-back" aria-label="Card back">
    <div class="back-mark">Faraway Nest Seekers</div>
    <div class="back-text">
      <p class="heading">What does your dream house have:</p>
      <ul class="wishlist">
        <li>swimming pool <svg class="tick" viewBox="0 0 13 11"><path d="M1 6 L5 10 L12 1" fill="none" stroke="#e8603a" stroke-width="2"/></svg></li>
        <li>private vineyard <svg class="tick" viewBox="0 0 13 11"><path d="M1 6 L5 10 L12 1" fill="none" stroke="#e8603a" stroke-width="2"/></svg></li>
        <li>herb garden <svg class="tick" viewBox="0 0 13 11"><path d="M1 6 L5 10 L12 1" fill="none" stroke="#e8603a" stroke-width="2"/></svg></li>
        <li>full sized football pitch <svg class="tick" viewBox="0 0 13 11"><path d="M1 6 L5 10 L12 1" fill="none" stroke="#e8603a" stroke-width="2"/></svg></li>
      </ul>
      <p class="heading underlined">How to buy a home abroad:</p>
      <p class="method">Method 1:</p>
      <ol class="steps">
        <li>1) Scour internet for suitable estate agents</li>
        <li>2) Arrange hectic holiday timetable with multiple agents in multiple languages</li>
        <li>3) Fly to destination to find property was not as it seemed</li>
        <li>4) Feel frustrated and helpless</li>
      </ol>
      <p class="or">OR</p>
      <p class="method">Method 2:</p>
      <p>Contact your expert home hunter (details overleaf) - and leave the hard work to them</p>
    </div>
  </section>

  <!-- front -->
  <section class="card card-front" aria-label="Card front">
    <div class="front-top">
      <span class="brand-dot"></span>
      <span class="brand-name">Faraway Nest Seekers</span>
    </div>
    <div class="front-stripe"></div>
    <div class="front-band">
      <div class="person">
        <p class="person-name">Gordon Marsh</p>
        <p class="person-role">founder</p>
      </div>
      <span class="divider"></span>
      <ul class="contacts">
        <li><svg class="contact-icon" viewBox="0 0 14 14"><path d="M3 1 L5.5 1 L6.5 4 L5 5.3 Q6.5 8.5 8.7 9 L10 7.5 L13 8.5 L13 11 Q12.5 13 10.5 13 Q2 12 1 3.5 Q1 1.5 3 1Z" fill="#e2582e"/></svg>140 555 0182</li>
        <li><svg class="contact-icon" viewBox="0 0 14 14"><path d="M3 1 L5.5 1 L6.5 4 L5 5.3 Q6.5 8.5 8.7 9 L10 7.5 L13 8.5 L13 11 Q12.5 13 10.5 13 Q2 12 1 3.5 Q1 1.5 3 1Z" fill="#e2582e"/></svg>555 301 447</li>
        <li><svg class="contact-icon" viewBox="0 0 14 14"><circle cx="7" cy="7" r="6" fill="#e2582e"/><path d="M1 7 H13 M7 1 V13 M7 1 Q3 7 7 13 M7 1 Q11 7 7 13" fill="none" stroke="#4a4440" stroke-width="1"/></svg>www.quillan-tarvo.com</li>
        <li><svg class="contact-icon" viewBox="0 0 14 14"><rect x="1" y="3" width="12" height="9" rx="1" fill="#e2582e"/><path d="M1.5 3.5 L7 8 L12.5 3.5" fill="none" stroke="#4a4440" stroke-width="1.2"/></svg>info@quillan-tarvo.com</li>
      </ul>
    </div>
  </section>

</main>
</body>
</html>
```